Butcher shop

We have 2 butcher shops:

Shop 9, Ridgeway Court, Aberdeen NSW 2336
Ph 02 6512 3840

47 Marlow St, Scone NSW 2337
Ph 02 6518 2274

ABN 48 907 215 816

I would like this info on reverse of card and my personal info on front of card. I have a logo I would like to use also. Require a very smooth thick matte card, with colour both sides.

Front of card should say:

Linda Farrugia
Accounts

Ph 0437 620 915
E lindafarrugia@quollmail.com.au

Industry/Entity Type

Shop

Contact Information for Business Card

Linda Farrugia
Ph 0437 620 915

Logo Text

Farrugia's Quality Meats

Logo styles of interest
Pictorial/Combination Logo
Requirements
Must have
• We use Century Gothic Font

```html
<!DOCTYPE html>
<html lang="en">
<head>
<meta charset="utf-8">
<title>Farrugia's Quality Meats – Business Card</title>
<link rel="stylesheet" href="https://fonts.googleapis.com/css2?family=Questrial&family=Mulish:wght@700;800&display=swap">
<style>
  :root {
    --canvas: #ffffff;
    --sky: #8fd8f4;
    --ink: #231f20;
    --card-edge: #e6e7e8;
    --rule: #6d6e70;
  }
  * { margin: 0; padding: 0; box-sizing: border-box; }
  html, body {
    width: 900px; height: 1200px; overflow: hidden;
    background: var(--canvas);
  }
  .canvas { position: relative; width: 900px; height: 1200px; color: var(--ink); }

  .card { position: absolute; left: 14px; width: 872px; text-align: center; }

  /* Front */
  .card-front {
    top: 76px; height: 492px;
    border: 3px solid var(--card-edge);
    background: #fff;
  }
  .brand {
    position: absolute; left: 310px; top: 36px; width: 248px; height: 190px;
    display: flex; flex-direction: column; align-items: center; justify-content: flex-end;
    gap: 22px; padding-bottom: 14px;
  }
  .brand-square { width: 64px; height: 64px; background: var(--sky); flex: none; }
  .brand-name {
    font-family: "Questrial", sans-serif; font-size: 32px; line-height: 36px;
    color: var(--ink); text-align: center; white-space: nowrap;
  }
  .divider {
    position: absolute; left: 368px; top: 262px; width: 134px; height: 3px;
    background: var(--rule);
  }
  .person-name {
    position: absolute; left: 0; right: 0; top: 288px;
    font-family: "Mulish", sans-serif; font-weight: 800; font-size: 25px;
    letter-spacing: 1px;
  }
  .person-role {
    position: absolute; left: 0; right: 0; top: 320px;
    font-family: "Questrial", sans-serif; font-size: 27px;
  }
  .contact {
    position: absolute; left: 0; right: 0;
    font-family: "Questrial", sans-serif; font-size: 28px;
  }
  .contact-phone { top: 386px; }
  .contact-email { top: 420px; }
  .contact-key {
    color: var(--sky); font-family: "Mulish", sans-serif; font-weight: 800;
    margin-right: 12px;
  }

  /* Back */
  .card-back {
    top: 617px; left: 16px; width: 870px; height: 489px;
    background: var(--sky);
  }
  .shop {
    position: absolute; left: 0; right: 0;
    font-family: "Mulish", sans-serif; font-weight: 800; font-size: 25px; line-height: 33px;
  }
  .shop-aberdeen { top: 112px; }
  .shop-scone { top: 280px; }
  .abn {
    position: absolute; left: 0; right: 0; top: 408px;
    font-family: "Questrial", sans-serif; font-size: 23px;
  }
</style>
</head>
<body>
<main class="canvas">
  <section class="card card-front">
    <div class="brand">
      <span class="brand-square"></span>
      <span class="brand-name">Farrugia's<br>Quality Meats</span>
    </div>
    <div class="divider" role="img" aria-label="Decorative divider ornament"></div>
    <h1 class="person-name">LINDA FARRUGIA</h1>
    <p class="person-role">Accounts</p>
    <p class="contact contact-phone"><span class="contact-key">t</span>0437 620 915</p>
    <p class="contact contact-email"><span class="contact-key">e</span>lindafarrugia@quollmail.com.au</p>
  </section>

  <section class="card card-back">
    <p class="shop shop-aberdeen">Shop 9, Ridgeway Court, Aberdeen NSW 2336<br>Ph 02 6512 3840</p>
    <p class="shop shop-scone">47 Marlow St, Scone NSW 2337<br>Ph 02 6518 2274</p>
    <p class="abn">ABN 48 907 215 816</p>
  </section>
</main>
</body>
</html>
```